Breakthrough memory supplement needs an eye catching label design

Brightvale Goods, LLC needs an eye catching label design for Cortivane, an Advanced Brain and Memory Formula

Completed label designs should be saved as .EPS files with all fonts outlined.
We can also accept Adobe Photoshop or .JPG files at 300dpi.
All files MUST include the .0625 bleed on all sides.

Target Market(s)

people 45 and older that are noticing there memory is not as good as it once was

Industry/Entity Type

Supplement

Colors

Designer to choose colors to be used in the design.

Requirements
Must have
• Cortivane
• Advanced Brain and Memory Formula
Nice to have
• look sciencey/ medical
Should not have
• cutesy

```html
<!DOCTYPE html>
<html lang="en">
<head>
<meta charset="utf-8">
<title>Cortivane Label</title>
<link href="https://fonts.googleapis.com/css2?family=Arimo:wght@400;700&family=Archivo:wght@800&family=Bebas+Neue&family=Montserrat:wght@600&family=Roboto+Condensed:wght@700&display=swap" rel="stylesheet">
<style>
  :root {
    --teal: #4fe0d1;
    --teal-soft: #d9f6f8;
    --ink: #5f6062;
    --ink-dark: #4a4b4d;
    --orange: #f07c2c;
    --blue-frame: #94bde3;
    --paper: #ffffff;
  }
  * { box-sizing: border-box; margin: 0; padding: 0; }
  html, body { width: 1200px; height: 1000px; overflow: hidden; background: var(--paper); }
  .canvas { position: relative; width: 1200px; height: 1000px; font-family: "Arimo", Arial, sans-serif; color: var(--ink); }

  .bleed-frame { position: absolute; left: 24px; top: 251px; width: 1153px; height: 431px; border: 1px solid var(--blue-frame); }
  .trim-frame { position: absolute; left: 34px; top: 261px; width: 1133px; height: 410px; border: 2px solid var(--orange); }

  /* Left panel */
  .directions { position: absolute; left: 47px; top: 285px; width: 272px; font-size: 9.6px; line-height: 11.6px; text-align: justify; }
  .directions p { margin-bottom: 11.6px; }
  .directions strong { font-weight: 700; }
  .fda-note { position: absolute; left: 48px; top: 543px; width: 229px; height: 36px; border: 2px solid var(--ink); padding: 2px 4px; font-size: 8px; line-height: 10px; font-weight: 700; }
  .distributor { position: absolute; left: 50px; top: 597px; font-family: "Roboto Condensed", "Arial Narrow", sans-serif; font-weight: 700; font-size: 14.5px; line-height: 17px; color: var(--ink); }

  /* Center brand */
  .brand-mark { position: absolute; left: 545px; top: 310px; width: 110px; height: 110px; border-radius: 50%; background: var(--teal-soft); border: 2px solid var(--teal); }
  .brand-name { position: absolute; left: 340px; width: 520px; top: 447px; text-align: center; font-family: "Bebas Neue", "Oswald", sans-serif; font-size: 116px; line-height: 100px; letter-spacing: 5px; color: var(--teal); }
  .tagline { position: absolute; left: 340px; width: 520px; top: 543px; text-align: center; font-family: "Montserrat", Arial, sans-serif; font-weight: 600; font-size: 13.4px; letter-spacing: 1.6px; color: #9a9b9d; }
  .product-type { position: absolute; left: 440px; width: 320px; top: 593px; text-align: center; font-family: "Roboto Condensed", "Arial Narrow", sans-serif; font-weight: 700; font-size: 12.5px; line-height: 15.5px; letter-spacing: 0.6px; color: var(--teal); }

  /* Right panel */
  .facts { position: absolute; left: 870px; top: 290px; width: 269px; border: 1px solid var(--ink); padding: 1px 4px 2px 5px; font-size: 11px; line-height: 12.5px; }
  .facts-title { font-family: "Archivo", "Arial Black", sans-serif; font-weight: 800; font-size: 25px; line-height: 30px; color: var(--ink); letter-spacing: -0.2px; }
  .facts-serving { padding-left: 1px; }
  .facts-rule-thick { height: 5px; background: var(--ink); margin: 2px -1px 2px; }
  .facts-head { font-size: 9px; line-height: 11px; padding-bottom: 2px; letter-spacing: -0.2px; }
  .facts-rule { height: 2px; background: var(--ink); }
  .facts-row { display: grid; grid-template-columns: 1fr 50px 12px; border-bottom: 1px solid var(--ink); padding: 1px 0 0; }
  .facts-row .amt { text-align: right; }
  .facts-row .mark { text-align: right; }
  .facts-row .sub { grid-column: 1 / 4; padding-left: 6px; }
  .facts-foot { padding-top: 1px; }
  .other-info { position: absolute; left: 872px; top: 548px; width: 270px; font-size: 10.6px; line-height: 11.6px; text-align: justify; }
  .other-info strong { font-weight: 700; }
  .warnings { margin-top: 13px; font-weight: 700; text-align: justify; }
</style>
</head>
<body>
<div class="canvas">
  <div class="bleed-frame"></div>
  <div class="trim-frame"></div>

  <section class="directions">
    <p><strong>SUGGESTED USE:</strong> 1 capsule taken 1 to 2 times daily preferably with meals or as directed by a healthcare professional.</p>
    <p><strong>CAUTION:</strong> Do not exceed recommended dose. St. John's Wort may contribute to photosensitivity resulting in skin irritation and redness in persons exposed to strong sunlight or tanning booths. Avoid use in patients at risk of bleeding, taking anticoagulants, or with clotting disorders, based on case reports of bleeding. Discontinue use 2-3 weeks prior to some surgical and dental procedures due to increased risk of bleeding. Avoid use in couples who are trying to conceive, based on theoretical reduction of fertility. Pregnant or nursing mothers, children under 18, individuals with history of seizure, taking MAO inhibiting drugs, or with a known medical condition should consult a physician before using this or any dietary supplement. This product is manufactured and packaged in a facility which may also process milk, soy, wheat, egg, peanuts, tree nuts, fish and crustacean shellfish.</p>
  </section>

  <div class="fda-note">†These statements have not been evaluated by the Food &amp; Drug Administration. This product is not intended to diagnose, treat, cure or prevent any disease.</div>

  <div class="distributor">Distributed by:<br>Company Name<br>Full Address and Phone</div>

  <div class="brand-mark" aria-hidden="true"></div>
  <h1 class="brand-name">CORTIVANE</h1>
  <div class="tagline">ADVANCED BRAIN AND MEMORY FORMULA</div>
  <div class="product-type">DIETARY SUPPLEMENT<br>30 CAPSULES</div>

  <section class="facts">
    <div class="facts-title">Supplement Facts</div>
    <div class="facts-serving">Serving Size 1 Capsule<br>Servings Per Container: 30</div>
    <div class="facts-rule-thick"></div>
    <div class="facts-head">Amt Per Serv.&nbsp;&nbsp;&nbsp;%DV/RDI</div>
    <div class="facts-rule"></div>
    <div class="facts-row"><span><em>Ginkgo biloba</em> Leaf (24% extract)</span><span class="amt">50mg</span><span class="mark">*</span></div>
    <div class="facts-row"><span>Phosphatidylserine 4% Complex</span><span class="amt">125mg</span><span class="mark">*</span><span class="sub" style="padding-left:2px">(consisting of Lecithin and Phosphatidylserine)</span></div>
    <div class="facts-row"><span>N-Acetyl L-Carnitine HCl</span><span class="amt">50mg</span><span class="mark">*</span></div>
    <div class="facts-row"><span>St. John's Wort (0.3% extract)</span><span class="amt">250mg</span><span class="mark">*</span><span class="sub">(flower heads)</span></div>
    <div class="facts-row"><span>L-Glutamine</span><span class="amt">150mg</span><span class="mark">*</span></div>
    <div class="facts-row"><span><em>Bacopa monnieri</em> Leaf Extract</span><span class="amt">120mg</span><span class="mark">*</span><span class="sub">(20% bacosides)</span></div>
    <div class="facts-row"><span>Vinpocetine (seeds)</span><span class="amt">2mg</span><span class="mark">*</span></div>
    <div class="facts-row"><span>Huperzine-A (aerial plant)</span><span class="amt">10mcg</span><span class="mark">*</span></div>
    <div class="facts-foot">*Daily Value not established.</div>
  </section>

  <section class="other-info">
    <p><strong>Other ingredients:</strong> Gelatin (bovine), microcrystalline cellulose, vegetable magnesium stearate, and silicon dioxide.<br><strong>ALLERGEN WARNING: CONTAINS SOY (LECITHIN).</strong></p>
    <p class="warnings">KEEP OUT OF THE REACH OF CHILDREN.<br>DO NOT USE IF SAFETY SEAL IS DAMAGED OR MISSING. STORE IN A COOL, DRY PLACE.</p>
  </section>
</div>
</body>
</html>
```